Financial Advisor Resource Firm needs business card design

Need business card design for company in Omaha NE called Tallowbrook Partners. We provide resources to financial advisors....workshop programs, retirement analysis, and insurance planning. I would like to see designs that use grays, greens, black, and white colors. The final design should communicate 'collaboration' and be simple yet attractive to financial planning clients. I will attached our logo and another picture of a puzzle piece coming together. I would like the incorporate the puzzle picture somehow, maybe on the back somehow, with color or just the gray scale....OR, the picture be the front of the card with 'Tallowbrook' definition on it (see upload) and then company logo, employee name, title, address on the back (see ppt uploaded). The following disclosure needs to be included somewhere- Advisory services offered through Marlowe Ridge Advisors, LLC.
Updates

I uploaded a svg and ai file of the logo

Target Market(s)

Financial planning clients and financial advisors....so pretty diverse age range of about 40-70.

Industry/Entity Type

Financial Planning

Contact Information for Business Card

Dennis K. Holloway, MBA
Founder/President
5727 E. Larkspur Avenue
Suite 418
Omaha, NE 68297
Phone- (402) 555-0147
Cell- (402) 555-0183
Fax- (402) 555-0129
email- dennis@tallowbrookgroup.example
web address- www.tallowbrookgroup.example

Colors
1b1b1b
474747
d3d3d3
ffffff
9bcb3c
abd036

Requirements
Must have
• Must include logo provided, must be 2 sided, and must have disclosure...all of these items listed in project description

```html
<!DOCTYPE html>
<html lang="en">
<head>
<meta charset="utf-8">
<title>Tallowbrook Partners – Business Card</title>
<link href="https://fonts.googleapis.com/css2?family=Open+Sans:wght@400;600;700&display=swap" rel="stylesheet">
<style>
  :root {
    --ink: #1b1b1b;
    --charcoal: #2a2a2a;
    --slate: #474747;
    --mist: #d3d3d3;
    --paper: #ffffff;
    --leaf: #9bcb3c;
    --leaf-deep: #5cb648;
    --lime: #abd036;
    --stage: #232323;
  }
  * { box-sizing: border-box; margin: 0; padding: 0; }
  html, body { width: 1200px; height: 900px; overflow: hidden; }
  body {
    background: var(--stage);
    font-family: "Open Sans", Arial, sans-serif;
    position: relative;
  }
  .card {
    position: absolute;
    left: 285px;
    width: 630px;
    height: 360px;
    overflow: hidden;
    box-shadow: 0 10px 28px rgba(0,0,0,.45);
  }
  .card--front { top: 60px; background: linear-gradient(160deg, var(--leaf-deep) 0%, #79bd46 55%, var(--leaf) 100%); }
  .card--back { top: 470px; background: var(--paper); }

  /* front */
  .front-band {
    position: absolute; top: 0; bottom: 0; left: 355px; width: 14px;
    background: var(--paper);
  }
  .front-plate {
    position: absolute; left: 110px; top: 130px; width: 410px; height: 100px;
    background: var(--paper); border-radius: 26px;
    display: flex; align-items: center; justify-content: center;
  }
  .brand-name {
    font-weight: 600; color: var(--ink); letter-spacing: .04em;
    font-size: 30px; white-space: nowrap;
  }

  /* back */
  .back-shape { position: absolute; inset: 0; }
  .name-tab {
    position: absolute; left: 0; top: 26px; width: 318px; height: 58px;
    background: var(--charcoal); border-radius: 0 29px 29px 0;
    display: flex; align-items: center; padding-left: 22px; gap: 18px;
    color: var(--paper);
  }
  .name-tab .person-name { font-weight: 700; font-size: 16px; line-height: 1.2; white-space: nowrap; }
  .name-tab .person-title { font-weight: 400; font-size: 15px; line-height: 1.2; }
  .contact-row {
    position: absolute; left: 0; display: flex; align-items: center;
    color: var(--paper); font-size: 13px; line-height: 1.35;
  }
  .contact-row .icon { width: 90px; display: flex; justify-content: center; }
  .row-address { top: 104px; }
  .row-phone { top: 178px; }
  .row-email { top: 262px; }
  .row-web { top: 318px; left: 90px; font-size: 12.5px; color: var(--paper); position: absolute; }
  .divider {
    position: absolute; left: 90px; height: 1.5px; background: var(--charcoal); opacity: .8;
  }
  .divider--one { top: 164px; width: 210px; }
  .divider--two { top: 246px; width: 240px; }
  .back-brand {
    position: absolute; left: 400px; top: 150px; width: 220px; text-align: center;
  }
  .back-brand .brand-name { font-size: 18px; letter-spacing: .03em; }
  .disclosure {
    position: absolute; right: 16px; bottom: 72px;
    font-size: 7px; color: var(--ink); white-space: nowrap;
  }
</style>
</head>
<body>

<section class="card card--front" aria-label="Card front">
  <div class="front-band"></div>
  <div class="front-plate">
    <span class="brand-name">Tallowbrook Partners</span>
  </div>
</section>

<section class="card card--back" aria-label="Card back">
  <svg class="back-shape" width="630" height="360" viewBox="0 0 630 360" aria-hidden="true">
    <defs>
      <linearGradient id="leafFill" x1="0" y1="1" x2="1" y2="0">
        <stop offset="0" stop-color="#9bcb3c"/>
        <stop offset="1" stop-color="#5cb648"/>
      </linearGradient>
    </defs>
    <path d="M0 0 H260 Q320 0 345 60 L385 290 Q398 360 440 360 H0 Z" fill="url(#leafFill)"/>
    <path d="M272 0 Q334 0 359 60 L399 290 Q411 352 452 360" fill="none" stroke="#5cb648" stroke-width="4"/>
  </svg>

  <div class="name-tab">
    <svg width="26" height="26" viewBox="0 0 26 26" aria-hidden="true">
      <circle cx="13" cy="8" r="6" fill="#fff"/>
      <path d="M2 26 Q2 15 13 15 Q24 15 24 26 Z" fill="#fff"/>
    </svg>
    <div>
      <div class="person-name">Dennis K. Holloway, MBA</div>
      <div class="person-title">Founder/President</div>
    </div>
  </div>

  <div class="contact-row row-address">
    <span class="icon">
      <svg width="16" height="22" viewBox="0 0 16 22" aria-hidden="true">
        <path d="M8 1 C3.5 1 1 4.3 1 7.8 C1 12.5 8 21 8 21 C8 21 15 12.5 15 7.8 C15 4.3 12.5 1 8 1 Z" fill="none" stroke="#fff" stroke-width="2"/>
        <circle cx="8" cy="8" r="2.4" fill="#fff"/>
      </svg>
    </span>
    <span>5727 E. Larkspur Avenue<br>Suite 418<br>Omaha, NE 68297</span>
  </div>
  <div class="divider divider--one"></div>

  <div class="contact-row row-phone">
    <span class="icon">
      <svg width="20" height="20" viewBox="0 0 20 20" aria-hidden="true">
        <path d="M4 1 L7.5 5 L5.5 7.5 Q7.5 12 12.5 14.5 L15 12.5 L19 16 L16.5 19 Q8 18 2 9 Q0.5 4.5 4 1 Z" fill="#fff"/>
      </svg>
    </span>
    <span>Phone- (402) 555-0147<br>Cell- (402) 555-0183<br>Fax- (402) 555-0129</span>
  </div>
  <div class="divider divider--two"></div>

  <div class="contact-row row-email">
    <span class="icon">
      <svg width="24" height="16" viewBox="0 0 24 16" aria-hidden="true">
        <rect x="1" y="1" width="22" height="14" fill="none" stroke="#fff" stroke-width="2"/>
        <path d="M1 1 L12 9 L23 1" fill="none" stroke="#fff" stroke-width="2"/>
      </svg>
    </span>
    <span>dennis@tallowbrookgroup.example</span>
  </div>

  <div class="row-web">www.tallowbrookgroup.example</div>

  <div class="back-brand">
    <span class="brand-name">Tallowbrook Partners</span>
  </div>
  <p class="disclosure">Advisory services offered through Marlowe Ridge Advisors, LLC.</p>
</section>

</body>
</html>
```